Business Card for Coach - ready to print

Design Business Card ready to order prints www.lukasbrenner.coach

* An Overview / Background of the Business & Services
· Coaching
· Personal growth
* The Target Market / Audience you are trying to reach
· private person in different roles (self, familiy, business role)s
* Design Specifics; any preferences or ideas for Style, Colour, Imagery, etc
· See www.lukasbrenner.coach
· "simple" design
· (small) element of surprise / unusual element

* Information that will be placed in the Business Card
· Beratung und Coaching
· Address: Lukas Brenner, Talmatt 42, CH-8531 Winterthur, Mobile +41 76 254 63 07
* Do you have an existing website or Facebook page where designers can learn more about your company?
· lukasbrenner.coach

Target Market(s)

private person in different roles (self, familiy, business role)

Industry/Entity Type

Life Coaching

Contact Information for Business Card

Lukas Brenner
Talmatt 42
CH-8531 Winterthur

Mobile: +41 76 254 63 07
Email: lubr@sonnwelt.ch
www.lukasbrenner.coach

Font styles to use
Sans Serif

Colors

Designer to choose colors to be used in the design.

Requirements
Must have
• "simple" design
• element of surprise / unusual element
• Beratung & Coaching
• see www.lukasbrenner.coach for colors and so...
Nice to have
• TA Symbol (three rings on top of each other) - unsual presentation
• QR Code of Website (see if it fits in and still looks good).

```html
<!DOCTYPE html>
<html lang="de">
<head>
<meta charset="utf-8">
<title>Lukas Brenner – Visitenkarte</title>
<link rel="stylesheet" href="https://fonts.googleapis.com/css2?family=Jost:wght@600&family=Questrial&display=swap">
<style>
  :root {
    --page-bg: #c8c8c8;
    --card-blue: #b7e0f7;
    --ink-dark: #1c1c1c;
    --ink-text: #4a4a4a;
    --photo-light: #a9adb1;
    --photo-dark: #6f7479;
  }
  * { margin: 0; padding: 0; box-sizing: border-box; }
  html, body {
    width: 1125px; height: 1200px; overflow: hidden;
    background: var(--page-bg);
  }
  .card {
    position: absolute; left: 178px; width: 768px; height: 437px;
    background: var(--card-blue);
    box-shadow: 0 4px 12px rgba(0,0,0,.25);
    overflow: hidden;
  }
  .card-front { top: 140px; border-radius: 24px; }
  .card-back { top: 626px; }

  .name-band { position: absolute; left: 0; top: 0; width: 768px; height: 437px; }
  .name {
    position: absolute; left: 62px; top: 115px;
    font-family: "Jost", sans-serif; font-weight: 600;
    font-size: 40px; line-height: 1; color: var(--card-blue);
    letter-spacing: 0.2px;
  }
  .address, .contact {
    position: absolute; left: 62px;
    font-family: "Questrial", sans-serif; color: var(--ink-text);
    font-size: 19px; line-height: 22px;
  }
  .address { top: 257px; }
  .contact { top: 314px; list-style: none; }
  .contact li { display: flex; align-items: center; height: 28.5px; }
  .contact svg { width: 13px; height: 13px; margin-right: 8px; flex: none; }

  .tagline {
    position: absolute; left: 0; right: 0; top: 190px;
    text-align: center;
    font-family: "Jost", sans-serif; font-weight: 600;
    font-size: 42px; line-height: 1; color: var(--ink-dark);
  }
</style>
</head>
<body>
  <section class="card card-front">
    <svg class="name-band" viewBox="0 0 768 437" aria-hidden="true">
      <defs>
        <radialGradient id="portrait-tone" cx="50%" cy="40%" r="60%">
          <stop offset="0" stop-color="var(--photo-light)"/>
          <stop offset="1" stop-color="var(--photo-dark)"/>
        </radialGradient>
      </defs>
      <rect x="0" y="101" width="579" height="84" fill="var(--ink-dark)"/>
      <circle cx="635" cy="143" r="70" fill="var(--card-blue)"/>
    </svg>
    <svg style="position:absolute;left:571px;top:79px;width:128px;height:128px" viewBox="0 0 128 128" role="img" aria-label="Porträtfoto von Lukas Brenner">
      <circle cx="64" cy="64" r="64" fill="url(#portrait-tone)"/>
    </svg>
    <h1 class="name">Lukas Brenner</h1>
    <address class="address" style="font-style:normal">
      Talmatt 42<br>CH-8531 Winterthur
    </address>
    <ul class="contact">
      <li>
        <svg viewBox="0 0 24 24" aria-hidden="true"><path fill="var(--ink-dark)" d="M6.6 10.8a15.1 15.1 0 0 0 6.6 6.6l2.2-2.2c.3-.3.7-.4 1-.2 1.1.4 2.3.6 3.6.6.6 0 1 .4 1 1V20c0 .6-.4 1-1 1A17 17 0 0 1 3 4c0-.6.4-1 1-1h3.5c.6 0 1 .4 1 1 0 1.3.2 2.5.6 3.6.1.3 0 .7-.2 1z"/></svg>
        +41 76 254 63 07
      </li>
      <li>
        <svg viewBox="0 0 24 24" aria-hidden="true"><rect x="2" y="5" width="20" height="14" fill="var(--ink-dark)"/><path d="M4 7l8 6 8-6" stroke="var(--card-blue)" stroke-width="2" fill="none"/></svg>
        lubr@sonnwelt.ch
      </li>
      <li>
        <svg viewBox="0 0 24 24" aria-hidden="true"><circle cx="12" cy="12" r="10" fill="var(--ink-dark)"/><path d="M2 12h20M12 2c3 3 3 17 0 20M12 2c-3 3-3 17 0 20" stroke="var(--card-blue)" stroke-width="1.5" fill="none"/></svg>
        www.lukasbrenner.coach
      </li>
    </ul>
  </section>

  <section class="card card-back">
    <p class="tagline">Beratung &amp; Coaching</p>
  </section>
</body>
</html>
```